Business Card Design Project

Financial planning, Insurance and Real estate - Financial Services company

Contact Information for Business Card

Looking for something simple in design -
Tolverin Equity LLC
Tolverin Wealth Managment

```html
<!DOCTYPE html>
<html lang="en">
<head>
<meta charset="utf-8">
<title>Tolverin Wealth Management – Business Card</title>
<link rel="stylesheet" href="https://fonts.googleapis.com/css2?family=Anton&family=Roboto+Condensed:wght@700&display=swap">
<style>
  :root {
    --card-blue: #1a7ab2;
    --ink-white: #ffffff;
  }
  * { margin: 0; padding: 0; box-sizing: border-box; }
  html, body {
    width: 1200px;
    height: 720px;
    overflow: hidden;
    background: var(--card-blue);
  }
  .card {
    position: relative;
    width: 1200px;
    height: 720px;
    background: var(--card-blue);
    color: var(--ink-white);
    font-family: "Roboto Condensed", "Arial Narrow", sans-serif;
    font-weight: 700;
  }
  .brand-mark {
    position: absolute;
    left: 514px;
    top: 148px;
    width: 150px;
    height: 150px;
    border: 5px solid var(--ink-white);
    border-radius: 50%;
  }
  .brand-name {
    position: absolute;
    left: 0;
    width: 1178px;
    top: 388px;
    text-align: center;
    font-family: "Anton", Impact, sans-serif;
    font-weight: 400;
    font-size: 30px;
    letter-spacing: 0.2px;
  }
  .holder {
    position: absolute;
    left: 257px;
    width: 320px;
    top: 486px;
    text-align: center;
    line-height: 1.05;
  }
  .holder-name { font-size: 36px; }
  .holder-role { font-size: 30px; }
  .divider {
    position: absolute;
    left: 572px;
    top: 462px;
    width: 2px;
    height: 122px;
    background: var(--ink-white);
  }
  .contact {
    position: absolute;
    left: 628px;
    display: flex;
    align-items: center;
    gap: 14px;
    font-size: 27px;
  }
  .contact-phone { top: 474px; }
  .contact-email { top: 526px; }
  .contact svg { flex: none; }
</style>
</head>
<body>
  <main class="card">
    <div class="brand-mark" aria-hidden="true"></div>
    <p class="brand-name">Tolverin Wealth Management</p>

    <div class="holder">
      <p class="holder-name">Name Surname</p>
      <p class="holder-role">Designation</p>
    </div>

    <div class="divider" aria-hidden="true"></div>

    <p class="contact contact-phone">
      <svg width="26" height="28" viewBox="0 0 24 24" aria-hidden="true">
        <path fill="#ffffff" d="M6.6 10.8a15.1 15.1 0 0 0 6.6 6.6l2.2-2.2a1 1 0 0 1 1-.25 11.4 11.4 0 0 0 3.6.57 1 1 0 0 1 1 1V20a1 1 0 0 1-1 1A17 17 0 0 1 3 4a1 1 0 0 1 1-1h3.5a1 1 0 0 1 1 1c0 1.25.2 2.45.57 3.57a1 1 0 0 1-.25 1z"/>
      </svg>
      <span>000-123-4567</span>
    </p>

    <p class="contact contact-email">
      <svg width="34" height="24" viewBox="0 0 34 24" aria-hidden="true">
        <rect x="1" y="1" width="32" height="22" fill="#ffffff"/>
        <path d="M2 2 L17 14 L32 2 M2 22 L13 11 M32 22 L21 11" fill="none" stroke="#1a7ab2" stroke-width="2"/>
      </svg>
      <span>name@companyname.com</span>
    </p>
  </main>
</body>
</html>
```